Logo & Responsive Website Design for Mortgage Company

Vantor Mortgage is a new Mortgage Fin-Tech company that will use its own innovative, proprietary technology for lead generation, mortgage origination, and processing of residential home loans in the US. The design should convey that we are a technology-driven company, offering borrowers seeking home loans an exceptional experience throughout the borrowing process.

We are looking for designs that are elegant, convey technical competency, simple to navigate, and set us apart from the competition.

We are not set on any particular colors at this point, so feel free to choose the best colors for your particular designs.

Please include both desktop and mobile designs.

Some Examples of Mortgage Websites. These are to show the typical content, not designs that we particularly like or dislike.
https://www.plumvane.com/
https://www.qbtfunding.com/
https://dorvelmortgage.com/
https://kelvo.com/
https://corvabaylending.com/

Please send comments with additional questions.

Thank You For your participation.

Target Market(s)

U.S. Residential Home Loan Seekers

Industry/Entity Type

FinTech Mortgage

Number of Pages Required

2 page

```html
<!DOCTYPE html>
<html lang="en">
<head>
<meta charset="utf-8">
<title>Vantor Mortgage</title>
<link href="https://fonts.googleapis.com/css2?family=Montserrat:wght@600;700;800&family=Poppins:wght@400;500;600&display=swap" rel="stylesheet">
<style>
:root{
  --green:#1fbf83;
  --green-dark:#17a370;
  --green-soft:#d9f5ea;
  --ink:#111418;
  --text:#555b63;
  --muted:#9aa0a6;
  --line:#e4e7ea;
  --black:#0b0b0c;
  --blush:#f6eef2;
  --white:#ffffff;
}
*{box-sizing:border-box;margin:0;padding:0}
html,body{width:1200px;height:4972px;overflow:hidden}
body{font-family:"Poppins",sans-serif;color:var(--text);background:var(--white);font-size:14px;line-height:1.6;position:relative}
h1,h2,h3,.brand{font-family:"Montserrat",sans-serif;color:var(--ink)}
.section{position:absolute;left:0;width:1200px}
.eyebrow{color:var(--green);font-size:14px;font-weight:500}
.btn{display:inline-block;padding:12px 26px;border-radius:4px;font-size:14px;font-weight:500;color:var(--white);background:var(--green)}
.btn-dark{background:var(--black)}
.photo{position:absolute}

/* header */
.header{top:0;height:100px;display:flex;align-items:center;padding:0 80px;border-bottom:1px solid var(--line)}
.brand{font-size:24px;font-weight:800;line-height:1.05;width:140px}
.nav{display:flex;gap:28px;margin-left:130px;font-size:14px;font-weight:500;color:var(--ink)}
.header-phone{margin-left:auto;display:flex;align-items:center;gap:8px;font-size:14px;color:var(--ink)}
.header .btn{margin-left:28px;padding:10px 18px}

/* hero */
.hero{top:100px;height:640px}
.hero .copy{position:absolute;left:80px;top:80px;width:470px}
.hero h1{font-size:50px;line-height:1.12;font-weight:800;margin:14px 0 18px}
.hero p{font-size:14px}
.hero .actions{margin-top:28px;display:flex;gap:16px}
.socials{display:flex;gap:12px;margin-top:30px}
.socials span{width:36px;height:36px;border-radius:50%;background:#c9cdd1}
.hero .bg-blob{right:0;top:0}
.hero .photo{left:700px;top:40px;width:460px;height:460px;border-radius:46% 54% 48% 52%/52% 44% 56% 48%;background:linear-gradient(135deg,#c7a98a,#556b85 60%,#2d3b4f)}
.play{position:absolute;left:830px;top:440px;width:88px;height:88px;border-radius:50%;background:var(--black);display:flex;align-items:center;justify-content:center}

/* calculator */
.calc{top:820px;left:80px;width:1040px;height:120px;background:var(--white);border-radius:8px;box-shadow:0 6px 30px rgba(0,0,0,.08);padding:20px 28px}
.calc h3{font-size:20px;color:var(--green);font-weight:700;border-bottom:1px solid var(--line);padding-bottom:8px}
.calc-row{display:flex;gap:24px;margin-top:12px;align-items:flex-end}
.field label{display:block;font-size:12px;font-weight:600;color:var(--ink)}
.field span{display:block;width:200px;height:36px;background:#eef0f2;border-radius:3px;font-size:11px;color:var(--muted);padding:8px 12px}
.calc .btn{padding:8px 24px}

/* about */
.about{top:1000px;height:400px}
.about .photo{left:80px;top:0;width:460px;height:380px;border-radius:50% 50% 44% 56%/56% 46% 54% 44%;background:linear-gradient(135deg,#9aa6b2,#d8c3a6 55%,#6d7a86)}
.about .copy{position:absolute;left:630px;top:10px;width:490px}
.about h2,.faq h2{font-size:34px;font-weight:800;line-height:1.2;margin:8px 0 14px}
.ticks{list-style:none;margin-top:16px}
.ticks li{display:flex;gap:10px;align-items:center;margin-bottom:8px;color:var(--ink)}

/* quote band */
.quote{top:1480px;height:320px;display:flex}
.quote .dark{width:600px;background:var(--black);padding:80px 80px}
.quote h2{color:var(--white);font-size:36px;font-weight:800}
.quote p{color:#c8cbce;margin:12px 0 28px;width:420px}
.quote .photo{position:static;width:600px;background:linear-gradient(160deg,#a9c6dd,#8a9a7c 55%,#4c4f4a)}

/* offer */
.offer{top:1880px;height:480px;text-align:center}
.offer h2{font-size:40px;font-weight:800;margin-top:6px}
.cards{position:absolute;left:80px;top:120px;display:flex;gap:30px}
.card{width:327px;height:355px;position:relative;text-align:left;overflow:hidden}
.card .photo{inset:0;width:100%;height:100%}
.card .shade{position:absolute;inset:0;background:linear-gradient(180deg,rgba(0,0,0,0) 40%,rgba(0,0,0,.85))}
.card h3{position:absolute;left:22px;bottom:52px;width:280px;color:var(--white);font-size:19px;font-weight:700;line-height:1.3}
.card a{position:absolute;left:22px;bottom:22px;color:var(--white);font-size:13px}

/* faq */
.faq{top:2440px;height:540px}
.faq .photo{left:80px;top:50px;width:440px;height:420px;border-radius:54% 46% 50% 50%/48% 52% 48% 52%;background:linear-gradient(135deg,#e8e2da,#b79a74 55%,#7a6a58)}
.faq .copy{position:absolute;left:630px;top:0;width:490px}
.acc{border-radius:4px;margin-bottom:16px;background:var(--green-soft);padding:14px 20px;display:flex;justify-content:space-between;align-items:center;color:var(--ink);font-weight:600;font-size:14px}
.acc.open{background:var(--green);color:var(--white)}
.acc-body{padding:0 20px 18px;font-size:13px}
.dot{width:22px;height:22px;border-radius:50%;background:var(--green);display:flex;align-items:center;justify-content:center}
.open .dot{background:var(--white)}

/* contact */
.contact{top:3060px;height:660px;background:var(--blush)}
.contact .photo{left:560px;top:0;width:640px;height:660px;background:linear-gradient(90deg,var(--blush),#c6d3e4 30%,#3f5f8e 75%,#2e4467)}
.contact .form{position:absolute;left:80px;top:120px;width:500px}
.contact h2{font-size:36px;font-weight:800;margin:6px 0 30px}
.grid{display:grid;grid-template-columns:1fr 1fr;gap:18px 20px}
.input label{display:block;font-weight:600;color:var(--ink);font-size:13px;margin-bottom:6px}
.input span{display:block;height:42px;background:#e4dde1;border-radius:3px;color:var(--muted);font-size:12px;padding:11px 14px}
.input.full{grid-column:1/3}
.input.full span{height:110px}
.contact .btn{margin-top:24px}

/* testimonial */
.testimonial{top:3800px;height:420px}
.testimonial .ring{left:80px;top:0;width:460px;height:400px;border-radius:50%;background:var(--green)}
.testimonial .photo{left:70px;top:20px;width:440px;height:380px;border-radius:48% 52% 50% 50%;background:linear-gradient(135deg,#d8d4cf,#5c5f66 50%,#2a2d33)}
.testimonial .copy{position:absolute;left:580px;top:50px;width:540px}
.testimonial h2{font-size:34px;font-weight:800;margin:6px 0 24px}
.person{display:flex;align-items:center;gap:16px;margin-bottom:14px}
.avatar{width:54px;height:54px;border-radius:50%;background:var(--green-soft)}
.person b{display:block;font-family:"Montserrat",sans-serif;color:var(--ink);font-size:16px}
.person small{font-size:12px}
.stars{display:flex;gap:4px;margin-top:16px}
.pager{display:flex;gap:6px;margin-top:24px}
.pager i{width:10px;height:10px;border-radius:50%;background:#cfd4d8}
.pager i:first-child{background:var(--green)}

/* newsletter */
.news{top:4320px;height:200px;background:linear-gradient(90deg,var(--green),#2ccf95 60%,#9fdcc4);display:flex;align-items:center;padding:0 80px}
.news h2{color:var(--white);font-size:34px;font-weight:800;line-height:1.2;width:500px}
.subscribe{margin-left:auto;display:flex;background:var(--white);border-radius:4px;padding:5px;width:490px}
.subscribe span{flex:1;padding:10px 14px;font-size:12px;color:var(--muted)}
.subscribe .btn{padding:8px 20px}

/* footer */
.footer{top:4520px;height:452px;background:var(--black);color:#c8cbce}
.footer .brand{color:var(--white);position:absolute;left:80px;top:70px;width:auto}
.footer .about-col{position:absolute;left:80px;top:140px;width:300px;font-size:13px}
.footer .socials{margin-top:22px}
.footer .socials span{background:transparent;border:1px solid #777}
.col{position:absolute;top:70px}
.col h4{font-family:"Montserrat",sans-serif;color:var(--white);font-size:18px;font-weight:700;margin-bottom:26px}
.col li{list-style:none;display:flex;align-items:center;gap:10px;font-size:13px;margin-bottom:14px}
.col li::before{content:"";width:8px;height:8px;border-radius:50%;background:var(--green)}
.addr li{align-items:flex-start}
.addr li::before{margin-top:6px}
.copyright{position:absolute;left:0;right:0;bottom:0;height:60px;border-top:1px solid #2a2c2e;text-align:center;line-height:60px;font-size:13px}
</style>
</head>
<body>

<header class="section header">
  <div class="brand">Vantor Mortgage</div>
  <nav class="nav"><span>Know Your Options</span><span>About Us</span><span>Reviews</span><span>Contact Us</span></nav>
  <div class="header-phone">
    <svg width="16" height="16" viewBox="0 0 24 24" fill="var(--ink)"><path d="M6.6 10.8a15 15 0 006.6 6.6l2.2-2.2a1 1 0 011-.25 11.4 11.4 0 003.6.57 1 1 0 011 1V20a1 1 0 01-1 1A17 17 0 013 4a1 1 0 011-1h3.5a1 1 0 011 1c0 1.25.2 2.45.57 3.57a1 1 0 01-.25 1z"/></svg>
    (+01) 555 018 42
  </div>
  <span class="btn">Calculator</span>
</header>

<section class="section hero">
  <svg class="photo bg-blob" width="560" height="620" viewBox="0 0 560 620"><path d="M140 0H560V560C480 600 380 560 330 500 260 420 120 420 90 320 60 220 160 160 140 0Z" fill="var(--green)"/></svg>
  <div class="copy">
    <div class="eyebrow">Welcome to Vantor Mortgage</div>
    <h1>Mortgage Is A Great For You</h1>
    <p>Lorem ipsum dolor sit amet, consectetur adipiscing elit. Cras quis nulla. Praesent fringilla erat ut consectetur commodo. Aenean risus risus, gravida in ornare vel, pretium sit amet ex. Integer non bibendum mi.</p>
    <div class="actions"><span class="btn">I'm purchasing</span><span class="btn btn-dark">I'm refinancing</span></div>
    <div class="socials"><span></span><span></span><span></span></div>
  </div>
  <div class="photo" role="img" aria-label="Photo of a couple meeting a mortgage advisor at a desk"></div>
  <div class="play"><svg width="26" height="26" viewBox="0 0 24 24"><path d="M8 5v14l11-7z" fill="#fff"/></svg></div>
</section>

<section class="section calc">
  <h3>Mortgage Calculator</h3>
  <div class="calc-row">
    <div class="field"><label>Total Amount</label><span>$0.00</span></div>
    <div class="field"><label>Down Payment</label><span>$0.00</span></div>
    <div class="field"><label>Interest Rate</label><span>0%</span></div>
    <div class="field"><label>Mortgage Period</label><span>Years</span></div>
    <span class="btn">Calculate</span>
  </div>
</section>

<section class="section about">
  <div class="photo" role="img" aria-label="Photo of a hand holding a phone with a small house model and keys"></div>
  <div class="copy">
    <div class="eyebrow">About Our Company</div>
    <h2>Vantor Mortgage is a new Mortgage Fin-Tech company</h2>
    <p>Vantor Mortgage is a new Mortgage Fin-Tech company that will use its own innovative, proprietary technology for lead generation, mortgage origination, and processing of residential home loans in the US.</p>
    <ul class="ticks">
      <li><svg width="16" height="16" viewBox="0 0 24 24"><path d="M4 12l5 5L20 6" stroke="var(--green)" stroke-width="3" fill="none"/></svg>Phasellus blandit porta lacus quis pellentesque.</li>
      <li><svg width="16" height="16" viewBox="0 0 24 24"><path d="M4 12l5 5L20 6" stroke="var(--green)" stroke-width="3" fill="none"/></svg>Phasellus in tempus mauris, nec mattis diam.</li>
      <li><svg width="16" height="16" viewBox="0 0 24 24"><path d="M4 12l5 5L20 6" stroke="var(--green)" stroke-width="3" fill="none"/></svg>Cras faucibus sodales nunc.</li>
    </ul>
  </div>
</section>

<section class="section quote">
  <div class="dark">
    <h2>Get Mortgage Quote</h2>
    <p>Lorem ipsum dolor sit amet, consectetur adipiscing elit, sed do eiusmod tempor incididunt ut labore et dolore.</p>
    <span class="btn">Get A Quote</span>
  </div>
  <div class="photo" role="img" aria-label="Photo of a happy couple in front of their new house"></div>
</section>

<section class="section offer">
  <div class="eyebrow">Why Choose Us</div>
  <h2>We Have Offer To You</h2>
  <div class="cards">
    <div class="card"><div class="photo" role="img" aria-label="Photo of a laptop showing lead generation" style="background:linear-gradient(135deg,#6f8f4a,#2f3f2a)"></div><div class="shade"></div><h3>Innovative, proprietary technology for lead generation</h3><a>Read More</a></div>
    <div class="card"><div class="photo" role="img" aria-label="Photo of a couple reviewing mortgage documents" style="background:linear-gradient(135deg,#d8b690,#7a5a40)"></div><div class="shade"></div><h3>Innovative, proprietary technology for mortgage origination</h3><a>Read More</a></div>
    <div class="card"><div class="photo" role="img" aria-label="Photo of an agent holding a small house model" style="background:linear-gradient(135deg,#eceae6,#9a9a9c)"></div><div class="shade"></div><h3>Processing of residential home loans in the US</h3><a>Read More</a></div>
  </div>
</section>

<section class="section faq">
  <div class="photo" role="img" aria-label="Photo of a hand placing coins beside a small house model"></div>
  <div class="copy">
    <div class="eyebrow">Frequently Asked Questions</div>
    <h2>Need Help? We're always here to guide you</h2>
    <div class="acc open">How Do You Qualify For A Loan? <span class="dot"><svg width="10" height="10" viewBox="0 0 10 10"><path d="M2 6l3-3 3 3" stroke="var(--green)" stroke-width="2" fill="none"/></svg></span></div>
    <p class="acc-body">Donec sollicitudin molestie malesuada. Vivamus magna justo, lacinia eget consectetur sed, convallis at tellus. Quisque velit nisi, pretium ut lacinia in, elementum id enim. Quisque velit nisi, pretium ut lacinia in, elementum id enim.</p>
    <div class="acc">A Good Lender Will Clearly Explain Mortgage? <span class="dot"><svg width="10" height="10" viewBox="0 0 10 10"><path d="M2 4l3 3 3-3" stroke="#fff" stroke-width="2" fill="none"/></svg></span></div>
    <div class="acc">How Much Home Can You Afford? <span class="dot"><svg width="10" height="10" viewBox="0 0 10 10"><path d="M2 4l3 3 3-3" stroke="#fff" stroke-width="2" fill="none"/></svg></span></div>
    <div class="acc">What does a Mortgage Advisor do? <span class="dot"><svg width="10" height="10" viewBox="0 0 10 10"><path d="M2 4l3 3 3-3" stroke="#fff" stroke-width="2" fill="none"/></svg></span></div>
  </div>
</section>

<section class="section contact">
  <div class="photo" role="img" aria-label="Photo of hands sheltering a small house model over documents"></div>
  <div class="form">
    <div class="eyebrow">Let's Contact</div>
    <h2>Contact With Us</h2>
    <div class="grid">
      <div class="input"><label>Name</label><span>Name</span></div>
      <div class="input"><label>Email</label><span>Email</span></div>
      <div class="input"><label>Phone</label><span>Phone</span></div>
      <div class="input"><label>Subject</label><span>Subject</span></div>
      <div class="input full"><label>Your Message</label><span>Your Message</span></div>
    </div>
    <span class="btn">Send Message</span>
  </div>
</section>

<section class="section testimonial">
  <div class="photo ring"></div>
  <div class="photo" role="img" aria-label="Photo of a handshake over a desk with a house model"></div>
  <div class="copy">
    <div class="eyebrow">Testimonials</div>
    <h2>People Are Saying About Us</h2>
    <div class="person"><div class="avatar"></div><div><b>Dana Ellery</b><small>United States</small></div></div>
    <p>Donec sollicitudin molestie malesuada. Vivamus magna justo, lacinia eget consectetur sed, convallis at tellus. Quisque velit nisi, pretium ut lacinia in, elementum id enim. Quisque velit nisi, pretium ut lacinia in, elementum id enim.</p>
    <div class="stars">
      <svg width="90" height="16" viewBox="0 0 90 16"><g fill="none" stroke="#f2b33d" stroke-width="1.2"><path id="s" d="M8 1l2.1 4.4 4.8.6-3.5 3.3.9 4.7L8 11.7 3.7 14l.9-4.7L1.1 6l4.8-.6z"/><use href="#s" x="18"/><use href="#s" x="36"/><use href="#s" x="54"/><use href="#s" x="72"/></g></svg>
    </div>
    <div class="pager"><i></i><i></i><i></i></div>
  </div>
</section>

<section class="section news">
  <h2>Do You Want to Get Update What's Upcoming?</h2>
  <div class="subscribe"><span>Enter your email</span><span class="btn">Subscribe</span></div>
</section>

<footer class="section footer">
  <div class="brand">Vantor<br>Mortgage</div>
  <div class="about-col">
    <p>Lorem ipsum dolor sit amet, consectetur adipiscing elit sed do eiusmod tempor incididunt ut labore et dolore.</p>
    <div class="socials"><span></span><span></span><span></span></div>
  </div>
  <div class="col" style="left:440px"><h4>Quick Links</h4><ul><li>Know Your Options</li><li>About Us</li><li>Reviews</li><li>Contact Us</li></ul></div>
  <div class="col" style="left:665px"><h4>Support</h4><ul><li>Contact</li><li>Our Blog</li><li>Privacy Policy</li><li>Terms &amp; Conditions</li></ul></div>
  <div class="col addr" style="left:905px;width:220px"><h4>Address</h4><ul><li>Enter your location here lorem ipsum</li><li>Phone:<br>(+01) 555 018 42</li><li>Email:<br>hello@vantormortgage.com</li></ul></div>
  <div class="copyright">Copyright © 2022 Vantor Mortgage</div>
</footer>

</body>
</html>
```